The Duchess of Nestwares is an online store specialising in all things for the home Bathroom, Kitchen,

I need a business card designed that is professional and elegant, yet not conservative. We will be wanting to brand the entire business and will have videos made where we will be interacting with the product, testing the products and basically creating an online interactive community for all those people interested in all things to do with the Home and the activities that take place in and around the home.

Target Market(s)

30-65yr old Men and Women who LOVE their Home and see it as their primary place of Happiness, their sanctuary!

Industry/Entity Type

Business

Contact Information for Business Card

www.duchessofnestwares.example The Duchess Of Nestwares-PO Box 58391, Mt Ferndale, Auckland. NEW ZEALAND. info@duchessofnestwares.example
Love your Home! Lorraine Becker-Duponte

Font styles to use
Decorative
Script

Colors
9bcb3b
33b8a4
85cae6
b7a5cd
eda3c7
e667a6
d2a4cc
fdf9cf
fee18a

Requirements
Must have
• Attractive colours. Must feel Elegant, yet simple. A font that is rounded without sharp edges. Organic feel to the card, something raw with texture.
Nice to have
• I like the logo deign that I gave in the photos, something feminine, but fun.
Should not have
• I dont like sharp edges, or linear design. I like organic, flowing, fractal type design. Something that looks beautiful in form when you look at it.

```html
<!DOCTYPE html>
<html lang="en">
<head>
<meta charset="utf-8">
<title>The Duchess of Nestwares — Business Card</title>
<link rel="stylesheet" href="https://fonts.googleapis.com/css2?family=Quicksand:wght@400;500;600&family=Dancing+Script:wght@600&display=swap">
<style>
  :root {
    --backdrop: #1c1d1d;
    --card-dark: #050505;
    --card-light: #ffffff;
    --ink-light: #ffffff;
    --ink-dark: #111111;
    --gold: #e9be3c;
    --rule: #8a8a8a;
    --pink: #e667a6;
  }
  * { margin: 0; padding: 0; box-sizing: border-box; }
  html, body {
    width: 1200px;
    height: 1000px;
    overflow: hidden;
    background: var(--backdrop);
  }
  .stage {
    position: relative;
    width: 1200px;
    height: 1000px;
  }
  .card {
    position: absolute;
    width: 680px;
    height: 390px;
    border-radius: 26px;
    box-shadow: 0 18px 40px rgba(0, 0, 0, 0.45);
  }
  .card--back {
    left: 430px;
    top: 130px;
    background: var(--card-dark);
  }
  .card--front {
    left: 150px;
    top: 480px;
    background: var(--card-light);
  }

  /* Back: brand name and postal address */
  .brand {
    position: absolute;
    left: 120px;
    top: 86px;
    width: 460px;
    font-family: "Quicksand", sans-serif;
    font-weight: 500;
    color: var(--ink-light);
    font-size: 56px;
    line-height: 1.1;
    letter-spacing: 1px;
  }
  .brand__mark {
    display: inline-block;
    width: 22px;
    height: 22px;
    border-radius: 50%;
    background: var(--gold);
    margin-left: 12px;
    vertical-align: middle;
  }
  .brand__rule {
    position: absolute;
    left: 120px;
    top: 236px;
    width: 440px;
    height: 2px;
    background: var(--rule);
  }
  .address {
    position: absolute;
    left: 120px;
    top: 252px;
    font-family: "Quicksand", sans-serif;
    font-weight: 500;
    font-size: 19px;
    color: var(--gold);
  }

  /* Front: personal details */
  .front__mark {
    position: absolute;
    left: 322px;
    top: 82px;
    width: 72px;
    height: 72px;
    border-radius: 50%;
    background: var(--pink);
  }
  .person {
    position: absolute;
    left: 0;
    top: 160px;
    width: 100%;
    text-align: center;
    font-family: "Quicksand", sans-serif;
    font-weight: 600;
    font-size: 40px;
    color: var(--ink-dark);
  }
  .tagline {
    position: absolute;
    left: 0;
    top: 206px;
    width: 100%;
    text-align: center;
    font-family: "Dancing Script", cursive;
    font-weight: 600;
    font-size: 40px;
    color: var(--ink-dark);
  }
  .contact {
    position: absolute;
    left: 50px;
    bottom: 44px;
    font-family: "Quicksand", sans-serif;
    font-weight: 500;
    font-size: 21px;
    color: var(--ink-dark);
  }
</style>
</head>
<body>
  <main class="stage">
    <section class="card card--back" aria-label="Business card, back">
      <div class="brand">The Duchess<span class="brand__mark"></span><br>of Nestwares</div>
      <div class="brand__rule"></div>
      <p class="address">PO Box 58391, Mt Ferndale, Auckland, New Zealand</p>
    </section>

    <section class="card card--front" aria-label="Business card, front">
      <div class="front__mark"></div>
      <h1 class="person">Lorraine Becker-Duponte</h1>
      <p class="tagline">Love your Home!</p>
      <p class="contact">info@duchessofnestwares.example | www.duchessofnestwares.example</p>
    </section>
  </main>
</body>
</html>
```